Theme and starter template for small business powerpoint deck

We are starting a technology consulting company and would like to have a powerpoint/google slide theme and initial template. We are more concerned with the theme/colors at this point. Initial template can be pretty simple. We would want a cover slide, agenda slide, some content slides including text content, image content, a combination of both, etc. A closing slide. we have included jpg files of our logo, let us know if you would prefer eps/vector. I assume you may want exact color data as well?

Target Market(s)

Technology and Customer Experience Leadership at companies with 25 or more employees

Industry/Entity Type

Technology Consulting

Font styles to use
Sans Serif

Colors
0054AA
0677BA
7BADD7
CADEEF
E8F1F8

Requirements
Must have
• I have attached JPG and EPS and vector files to project. I would like to stay with those colors but open to slight variation if recommended.

```html
<!DOCTYPE html>
<html lang="en">
<head>
<meta charset="utf-8">
<title>Veltrano Slide Theme</title>
<link href="https://fonts.googleapis.com/css2?family=Lato:wght@400;700;900&family=Nunito+Sans:wght@400;600;700&display=swap" rel="stylesheet">
<style>
:root{
  --board:#b5b5b9;
  --navy:#0054aa;
  --navy-deep:#004a96;
  --azure:#0677ba;
  --azure-deep:#056aa6;
  --sky:#7badd7;
  --mist:#cadeef;
  --ice:#e8f1f8;
  --ink:#1f1f24;
  --body:#3c3c44;
  --grey:#8f8f95;
  --white:#ffffff;
}
*{margin:0;padding:0;box-sizing:border-box}
html,body{width:1026px;height:1200px;overflow:hidden;background:var(--board)}
body{position:relative;font-family:'Nunito Sans',sans-serif;color:var(--ink)}
.slide{position:absolute;width:443px;height:249px;background:var(--white);overflow:hidden;box-shadow:0 6px 14px rgba(0,0,0,.22)}
.col-l{left:51px}.col-r{left:531px}
.row1{top:54px}.row2{top:335px}.row3{top:615px}.row4{top:896px}
.abs{position:absolute}
.band{position:absolute;left:0;top:0}
.band-title{position:absolute;left:26px;top:10px;color:var(--white);font-family:'Lato',sans-serif;font-weight:700;font-size:13px;letter-spacing:.2px}
.brand{position:absolute;right:26px;top:6px;font-family:'Lato',sans-serif;font-weight:900;font-size:19px;letter-spacing:1.2px;color:var(--ink);border-bottom:2px solid var(--grey);line-height:22px}
.brand.on-colour{color:var(--white);border-color:var(--white)}
.footer{position:absolute;right:26px;bottom:6px;display:flex;align-items:center;gap:5px;font-size:5.2px;color:var(--ink)}
.footer svg{display:block}
.footer .sep{margin:0 3px}
.page-no{width:11px;height:11px;transform:rotate(45deg);background:var(--grey);display:flex;align-items:center;justify-content:center;margin-left:6px}
.page-no span{transform:rotate(-45deg);color:var(--white);font-size:4.5px;font-weight:700}
.bullets{list-style:none;font-size:5px;line-height:8.3px;color:var(--body)}
.bullets li{position:relative;padding-left:11px;margin-bottom:4px}
.bullets li::before{content:"";position:absolute;left:0;top:2px;border-left:2.5px solid transparent;border-right:2.5px solid transparent;border-bottom:4px solid var(--azure)}
.photo{position:absolute}
.para{font-size:5px;line-height:8.3px;color:var(--body);text-align:justify;margin-bottom:6px}
.welcome{position:absolute;left:26px;top:96px;font-family:'Lato',sans-serif;font-size:8.5px;color:var(--grey)}
.cover-title{position:absolute;left:26px;top:106px;font-family:'Lato',sans-serif;font-weight:700;font-size:23px;color:var(--ink)}
.cover-rule{position:absolute;left:0;top:133px;width:67px;height:1.5px;background:var(--navy)}
.cover-lead{position:absolute;left:26px;top:144px;width:160px;font-size:5.8px;line-height:8.8px;color:var(--body)}
.cover-brand{position:absolute;left:26px;top:54px;font-family:'Lato',sans-serif;font-weight:900;font-size:9px;letter-spacing:.6px;color:var(--ink)}
.agenda-title{position:absolute;left:237px;top:50px;font-family:'Lato',sans-serif;font-size:16px;color:var(--ink)}
.agenda-rule{position:absolute;left:219px;top:70px;width:101px;height:1.5px;background:var(--navy)}
.agenda-list{position:absolute;left:237px;top:80px;list-style:none}
.agenda-list li{position:relative;padding-left:22px;height:23.8px;font-size:8.8px;line-height:14px;color:var(--ink)}
.agenda-list li::before{content:"";position:absolute;left:2px;top:4px;width:6px;height:6px;background:var(--azure);transform:rotate(45deg)}
.divider-title{position:absolute;left:0;width:100%;top:110px;text-align:center;font-family:'Lato',sans-serif;font-weight:700;font-size:24px;color:var(--white)}
.reason{position:absolute;top:64px;width:118px;text-align:center}
.reason .mark{width:28px;height:28px;border-radius:50%;margin:0 auto 10px}
.reason h3{font-family:'Lato',sans-serif;font-weight:700;font-size:7.4px;color:var(--ink);margin-bottom:4px}
.reason p{font-size:5px;line-height:8.3px;color:var(--body);margin-bottom:3px}
.ty-brand{position:absolute;left:25px;top:106px;font-family:'Lato',sans-serif;font-weight:900;font-size:25px;letter-spacing:1.6px;color:var(--white);border-bottom:2px solid var(--white);line-height:28px}
.ty-line{position:absolute;left:222px;top:76px;width:1px;height:97px;background:var(--white)}
.ty-title{position:absolute;left:242px;top:78px;font-family:'Lato',sans-serif;font-weight:700;font-size:19px;color:var(--white)}
.ty-list{position:absolute;left:242px;top:111px;list-style:none}
.ty-list li{display:flex;align-items:center;gap:7px;height:16px;font-size:7.4px;color:var(--white)}
</style>
</head>
<body>

<!-- Cover -->
<section class="slide col-l row1">
  <svg class="abs" width="443" height="249" viewBox="0 0 443 249">
    <defs>
      <linearGradient id="meetGrad" x1="0" y1="0" x2="1" y2="1">
        <stop offset="0" stop-color="#8a6a58"/><stop offset=".5" stop-color="#6c6f7c"/><stop offset="1" stop-color="#4a4038"/>
      </linearGradient>
    </defs>
    <polygon points="0,249 70,140 150,249" fill="var(--ice)"/>
    <polygon points="60,0 150,0 105,70" fill="var(--ice)"/>
    <polygon points="152,0 443,0 443,249 288,249" fill="url(#meetGrad)" role="img" aria-label="Photo of colleagues shaking hands across a meeting table"/>
    <polygon points="218,126 143,249 287,249" fill="var(--azure)"/>
  </svg>
  <div class="cover-brand">VELTRANO</div>
  <div class="welcome">WELCOME TO</div>
  <div class="cover-title">VELTRANO</div>
  <div class="cover-rule"></div>
  <p class="cover-lead">Lorem ipsum dolor sit amet, consectetur adipiscing elit, sed do eiusmod tempor incididunt ut labore et dolore magna aliqua. Ut enim ad minim veniam, quis nostrud exercitation ullamco laboris nisiea.</p>
</section>

<!-- Our features -->
<section class="slide col-r row1">
  <svg class="band" width="443" height="35" viewBox="0 0 443 35"><polygon points="0,0 280,0 248,35 0,35" fill="var(--navy)"/></svg>
  <div class="band-title">OUR FEATURES</div>
  <div class="brand">VELTRANO</div>
  <ul class="bullets abs" style="left:26px;top:62px;width:190px">
    <li>Lorem ipsum dolor sit amet, consectetur adipiscing elit, sed do eiusmod tempor incididunt ut labore et dolore magna aliqua. Ut enim ad minim veniam, quis nostrud exercitation ullamco laboris nisi ut aliquip ex ea commodo consequat. Duis aute irure dolor in reprehenderit in voluptate velit esse cillum dolore eu fugiat nulla pariaturea.</li>
    <li>Lorem ipsum dolor sit amet, consectetur adipiscing elit, sed do eiusmod tempor incididunt ut labore et dolore magna aliqua. Ut enim ad minim veniam, quis nostrudea.</li>
    <li>Lorem ipsum dolor sit amet, consectetur adipiscing elit, sed do eiusmod tempor incididunt ut labore et dolore magna aliqua. Ut enim ad minim veniam, quis nostrud exercitation ullamco laboris nisi ut aliquip ex ea commodo consequat. Duis aute irure dolor in reprehenderit in voluptate velit esse cillum dolore eu fugiat nulla pariaturea.</li>
    <li>Lorem ipsum dolor sit amet, consectetur adipiscing elit, sed do eiusmod tempor incididunt ut labore et dolore magna aliqua. Ut enim ad minim veniam, quis nostrudea.</li>
    <li>Lorem ipsum dolor sit amet, consectetur adipiscing elit, sed do eiusmod tempor incididunt ut labore et dolore magna aliquea.</li>
  </ul>
  <svg class="abs" style="left:225px;top:62px" width="210" height="160" viewBox="0 0 210 160">
    <polyline points="26,33 26,10 55,10" fill="none" stroke="var(--navy)" stroke-width="1.3"/>
    <polyline points="150,113 150,135 130,135" fill="none" stroke="var(--navy)" stroke-width="1.3"/>
  </svg>
  <div class="photo" style="left:236px;top:115px;width:123px;height:98px;background:linear-gradient(135deg,#6d6d6d,#d8d8d8)" role="img" aria-label="Black and white photo of hands using a tablet"></div>
  <div class="photo" style="left:293px;top:69px;width:123px;height:98px;background:linear-gradient(135deg,#2c3550,#7a6a62 60%,#c9a582);border:1.5px solid #fff" role="img" aria-label="Photo of a laptop with digital technology overlay"></div>
  <div class="footer">
    <svg width="5" height="5" viewBox="0 0 10 10"><path d="M2 0l2 2.5-1.2 1.3a6 6 0 0 0 3.4 3.4L7.5 6 10 8l-1.2 2C4 10 0 6 0 1.2z" fill="var(--azure)"/></svg>
    <span>+1 (555) 010 0199</span><span class="sep">|</span>
    <svg width="6" height="5" viewBox="0 0 12 9"><rect width="12" height="9" rx="1" fill="var(--azure)"/><path d="M0 1l6 4 6-4" stroke="#fff" fill="none"/></svg>
    <span>info@veltrano.com</span>
    <div class="page-no"><span>5</span></div>
  </div>
</section>

<!-- Agenda -->
<section class="slide col-l row2">
  <div class="abs" style="left:40px;top:0;width:179px;height:249px;background:var(--navy)"></div>
  <div class="abs" style="left:50px;top:41px;width:159px;height:187px;border:1.5px solid #fff"></div>
  <div class="photo" style="left:23px;top:30px;width:165px;height:189px;background:linear-gradient(160deg,#8e8c86,#5a5650 55%,#2e2c2a)" role="img" aria-label="Photo of two colleagues talking at an office table"></div>
  <div class="brand">VELTRANO</div>
  <div class="agenda-title">AGENDA</div>
  <div class="agenda-rule"></div>
  <ul class="agenda-list">
    <li>Lorem ipsum dolor sit</li>
    <li>Sed ut perspiciatis unde omnis istea</li>
    <li>Lorem ipsum dolor sit</li>
    <li>Sed ut perspiciatis unde omnis istea</li>
    <li>Lorem ipsum dolor sit</li>
    <li>Sed ut perspiciatis unde omnis istea</li>
  </ul>
  <div class="footer">
    <svg width="5" height="5" viewBox="0 0 10 10"><path d="M2 0l2 2.5-1.2 1.3a6 6 0 0 0 3.4 3.4L7.5 6 10 8l-1.2 2C4 10 0 6 0 1.2z" fill="var(--azure)"/></svg>
    <span>+1 (555) 010 0199</span><span class="sep">|</span>
    <svg width="6" height="5" viewBox="0 0 12 9"><rect width="12" height="9" rx="1" fill="var(--azure)"/><path d="M0 1l6 4 6-4" stroke="#fff" fill="none"/></svg>
    <span>info@veltrano.com</span>
    <div class="page-no"><span>2</span></div>
  </div>
</section>

<!-- Section divider -->
<section class="slide col-r row2" style="background:var(--navy)">
  <svg class="abs" width="443" height="249" viewBox="0 0 443 249">
    <polygon points="443,80 360,249 443,249" fill="var(--navy-deep)"/>
    <polygon points="400,40 443,40 443,120" fill="var(--navy-deep)" opacity=".6"/>
  </svg>
  <div class="brand on-colour">VELTRANO</div>
  <div class="divider-title">SECTION DIVIDER</div>
  <div class="footer" style="color:var(--white)">
    <svg width="5" height="5" viewBox="0 0 10 10"><path d="M2 0l2 2.5-1.2 1.3a6 6 0 0 0 3.4 3.4L7.5 6 10 8l-1.2 2C4 10 0 6 0 1.2z" fill="var(--sky)"/></svg>
    <span>+1 (555) 010 0199</span><span class="sep">|</span>
    <svg width="6" height="5" viewBox="0 0 12 9"><rect width="12" height="9" rx="1" fill="var(--sky)"/><path d="M0 1l6 4 6-4" stroke="var(--navy)" fill="none"/></svg>
    <span>info@veltrano.com</span>
    <div class="page-no" style="background:var(--white)"><span style="color:var(--ink)">6</span></div>
  </div>
</section>

<!-- Who we are -->
<section class="slide col-l row3">
  <svg class="band" width="443" height="35" viewBox="0 0 443 35"><polygon points="0,0 280,0 248,35 0,35" fill="var(--navy)"/></svg>
  <div class="band-title">WHO WE ARE</div>
  <div class="brand">VELTRANO</div>
  <div class="photo" style="left:25px;top:65px;width:169px;height:146px;background:linear-gradient(180deg,var(--navy) 0%,var(--sky) 45%,#b0b0b4 55%,var(--azure) 100%)" role="img" aria-label="Tinted photos of a team at work in blue, grey and light blue"></div>
  <div class="abs" style="left:222px;top:63px;width:195px">
    <p class="para">Lorem ipsum dolor sit amet, consectetur adipiscing elit, sed do eiusmod tempor incididunt ut labore et dolore magna aliqua. Ut enim ad minim veniam, quis nostrud exercitation ullamco laboris nisi ut aliquip ex ea commodo consequat. Duis aute irure dolor in reprehenderit in voluptate velit esse cillum dolore eu fugiat nulla pariatur. Excepteur sint occaecat cupidatat non proident, sunt in culpa qui officia deserunt mollit anim id est laborum.</p>
    <p class="para">Lorem ipsum dolor sit amet, consectetur adipiscing elit, sed do eiusmod tempor incididunt ut labore et dolore magna aliqua. Ut enim ad minim veniam, quis nostrud exercitation ullamco laboris nisi ut aliquip ex ea commodo consequat. Duis aute irure dolor in reprehenderit in voluptate velit esse cillum dolore eu fugiat nulla pariatura.</p>
    <p class="para">Lorem ipsum dolor sit amet, consectetur adipiscing elit, sed do eiusmod tempor incididunt ut labore et dolore magna aliqua. Ut enim ad minim veniam, quis nostrud exercitation ullamco laboris nisi ut aliquip ex ea commodo consequat. Duis aute irure dolor in reprehenderit in voluptate velit esse cillum dolore eu fugiat nulla pariatur. Excepteur sint occaecat cupidatat non proident, sunt in culpa qui officia deserunt mollit anim id est laborum.</p>
  </div>
  <div class="footer">
    <svg width="5" height="5" viewBox="0 0 10 10"><path d="M2 0l2 2.5-1.2 1.3a6 6 0 0 0 3.4 3.4L7.5 6 10 8l-1.2 2C4 10 0 6 0 1.2z" fill="var(--azure)"/></svg>
    <span>+1 (555) 010 0199</span><span class="sep">|</span>
    <svg width="6" height="5" viewBox="0 0 12 9"><rect width="12" height="9" rx="1" fill="var(--azure)"/><path d="M0 1l6 4 6-4" stroke="#fff" fill="none"/></svg>
    <span>info@veltrano.com</span>
    <div class="page-no"><span>3</span></div>
  </div>
</section>

<!-- Why choose -->
<section class="slide col-r row3">
  <svg class="band" width="443" height="35" viewBox="0 0 443 35"><polygon points="0,0 280,0 248,35 0,35" fill="var(--navy)"/></svg>
  <div class="band-title">WHY CHOOSE VELTRANO?</div>
  <div class="brand">VELTRANO</div>
  <div class="reason" style="left:23px">
    <div class="mark" style="background:var(--sky)"></div>
    <h3>LOREM IPSUM DOL</h3>
    <p>Lorem ipsum dolor sit amet, consectetur adipiscing elit, sed do eiusmod tempor incidi dunt ut labore et dolore magna aliqua. Ut enim ad minim veniam, quis nostrud exercitation ullamco laboris nisi ut aliquip ex ea commodo consequatea.</p>
    <p>Lorem ipsum dolor sit amet, consectetur adipiscing elit, sed do eiusmod tempor incidi dunt ut labore et dolore magna aliqua. Ut enim ad minim veniamea.</p>
  </div>
  <div class="reason" style="left:163px">
    <div class="mark" style="background:var(--navy)"></div>
    <h3>LOREM IPSUM DOL</h3>
    <p>Lorem ipsum dolor sit amet, consectetur adipiscing elit, sed do eiusmod tempor incidi dunt ut labore et dolore magna aliqua. Ut enim ad minim veniam, quis nostrud exercitation ullamco laboris nisi ut aliquip ex ea commodo consequatea.</p>
    <p>Lorem ipsum dolor sit amet, consectetur adipiscing elit, sed do eiusmod tempor incidi dunt ut labore et dolore magna aliqua. Ut enim ad minim veniamea.</p>
  </div>
  <div class="reason" style="left:302px">
    <div class="mark" style="background:var(--azure)"></div>
    <h3>LOREM IPSUM DOL</h3>
    <p>Lorem ipsum dolor sit amet, consectetur adipiscing elit, sed do eiusmod tempor incidi dunt ut labore et dolore magna aliqua. Ut enim ad minim veniam, quis nostrud exercitation ullamco laboris nisi ut aliquip ex ea commodo consequatea.</p>
    <p>Lorem ipsum dolor sit amet, consectetur adipiscing elit, sed do eiusmod tempor incidi dunt ut labore et dolore magna aliqua. Ut enim ad minim veniamea.</p>
  </div>
  <div class="footer">
    <svg width="5" height="5" viewBox="0 0 10 10"><path d="M2 0l2 2.5-1.2 1.3a6 6 0 0 0 3.4 3.4L7.5 6 10 8l-1.2 2C4 10 0 6 0 1.2z" fill="var(--azure)"/></svg>
    <span>+1 (555) 010 0199</span><span class="sep">|</span>
    <svg width="6" height="5" viewBox="0 0 12 9"><rect width="12" height="9" rx="1" fill="var(--azure)"/><path d="M0 1l6 4 6-4" stroke="#fff" fill="none"/></svg>
    <span>info@veltrano.com</span>
    <div class="page-no"><span>7</span></div>
  </div>
</section>

<!-- Our benefits -->
<section class="slide col-l row4">
  <svg class="band" width="443" height="35" viewBox="0 0 443 35"><polygon points="0,0 280,0 248,35 0,35" fill="var(--navy)"/></svg>
  <div class="band-title">OUR BENEFITS</div>
  <div class="brand">VELTRANO</div>
  <ul class="bullets abs" style="left:26px;top:62px;width:190px">
    <li>Lorem ipsum dolor sit amet, consectetur adipiscing elit, sed do eiusmod tempor incididunt ut labore et dolore magna aliqua. Ut enim ad minim veniam, quis nostrud exercitation ullamco laboris nisi ut aliquip ex ea commodo consequat. Duis aute irure dolor in reprehenderit in voluptate velit esse cillum dolore eu fugiat nulla pariatura.</li>
    <li>Lorem ipsum dolor sit amet, consectetur adipiscing elit, sed do eiusmod tempor incididunt ut labore et dolore magna aliqua. Ut enim ad minim veniam, quis nostrudea.</li>
    <li>Lorem ipsum dolor sit amet, consectetur adipiscing elit, sed do eiusmod tempor incididunt ut labore et dolore magna aliqua. Ut enim ad minim veniam, quis nostrud exercitation ullamco laboris nisi ut aliquip ex ea commodo consequat. Duis aute irure dolor in reprehenderit in voluptate velit esse cillum dolore eu fugiat nulla pariatura.</li>
    <li>Lorem ipsum dolor sit amet, consectetur adipiscing elit, sed do eiusmod tempor incididunt ut labore et dolore magna aliqua. Ut enim ad minim veniam, quis nostrudea.</li>
    <li>Lorem ipsum dolor sit amet, consectetur adipiscing elit, sed do eiusmod tempor incididunt ut labore et dolore magna aliquea.</li>
  </ul>
  <ul class="bullets abs" style="left:230px;top:62px;width:188px">
    <li>Lorem ipsum dolor sit amet, consectetur adipiscing elit, sed do eiusmod tempor incididunt ut labore et dolore magna aliqua. Ut enim ad minim veniam, quis nostrud exercitation ullamco laboris nisi ut aliquip ex ea commodo consequat. Duis aute irure dolor in reprehenderit in voluptate velit esse cillum dolore eu fugiat nulla pariatura.</li>
    <li>Lorem ipsum dolor sit amet, consectetur adipiscing elit, sed do eiusmod tempor incididunt ut labore et dolore magna aliqua. Ut enim ad minim veniam, quis nostrudea.</li>
    <li>Lorem ipsum dolor sit amet, consectetur adipiscing elit, sed do eiusmod tempor incididunt ut labore et dolore magna aliqua. Ut enim ad minim veniam, quis nostrud exercitation ullamco laboris nisi ut aliquip ex ea commodo consequat. Duis aute irure dolor in reprehenderit in voluptate velit esse cillum dolore eu fugiat nulla pariatura.</li>
    <li>Lorem ipsum dolor sit amet, consectetur adipiscing elit, sed do eiusmod tempor incididunt ut labore et dolore magna aliqua. Ut enim ad minim veniam, quis nostrudea.</li>
    <li>Lorem ipsum dolor sit amet, consectetur adipiscing elit, sed do eiusmod tempor incididunt ut labore et dolore magna aliquea.</li>
  </ul>
  <div class="footer">
    <svg width="5" height="5" viewBox="0 0 10 10"><path d="M2 0l2 2.5-1.2 1.3a6 6 0 0 0 3.4 3.4L7.5 6 10 8l-1.2 2C4 10 0 6 0 1.2z" fill="var(--azure)"/></svg>
    <span>+1 (555) 010 0199</span><span class="sep">|</span>
    <svg width="6" height="5" viewBox="0 0 12 9"><rect width="12" height="9" rx="1" fill="var(--azure)"/><path d="M0 1l6 4 6-4" stroke="#fff" fill="none"/></svg>
    <span>info@veltrano.com</span>
    <div class="page-no"><span>4</span></div>
  </div>
</section>

<!-- Thank you -->
<section class="slide col-r row4" style="background:var(--azure)">
  <svg class="abs" width="443" height="249" viewBox="0 0 443 249">
    <polygon points="443,90 360,249 443,249" fill="var(--azure-deep)"/>
    <polygon points="443,20 400,20 443,100" fill="var(--azure-deep)" opacity=".6"/>
  </svg>
  <div class="ty-brand">VELTRANO</div>
  <div class="ty-line"></div>
  <div class="ty-title">THANK YOU</div>
  <ul class="ty-list">
    <li><svg width="6" height="6" viewBox="0 0 10 10"><path d="M2 0l2 2.5-1.2 1.3a6 6 0 0 0 3.4 3.4L7.5 6 10 8l-1.2 2C4 10 0 6 0 1.2z" fill="#fff"/></svg>+1 (555) 010 0199</li>
    <li><svg width="6" height="5" viewBox="0 0 12 9"><rect width="12" height="9" rx="1" fill="#fff"/><path d="M0 1l6 4 6-4" stroke="var(--azure)" fill="none"/></svg>info@veltrano.com</li>
    <li><svg width="6" height="6" viewBox="0 0 10 10"><circle cx="5" cy="5" r="4.3" fill="none" stroke="#fff" stroke-width="1.2"/><path d="M1 5h8M5 1c-2 2.5-2 5.5 0 8M5 1c2 2.5 2 5.5 0 8" stroke="#fff" fill="none" stroke-width=".8"/></svg>www.veltrano.com</li>
    <li><svg width="5" height="7" viewBox="0 0 8 11"><path d="M4 0a4 4 0 0 1 4 4c0 3-4 7-4 7S0 7 0 4a4 4 0 0 1 4-4z" fill="#fff"/><circle cx="4" cy="4" r="1.5" fill="var(--azure)"/></svg>88 Harbor Lane, Springfield, United States</li>
  </ul>
</section>

</body>
</html>
```